Insurance Firm needs Stationary and Corporate Identity

We have a logo (provided) - we need a business card, letterhead, booklet cover, Benefit & Travel card design, and brand guide.
KTR (Kestrel Trust Reinsurers) is a National (Canadian) family-run benefits firm. We've been providing alternative benefit models to small and medium sized businesses for almost 25 years! Our goal is to create long-lasting customer relationships by partnering with our clients to become their dedicated benefits division instead of just selling a product to them.

Benefit & Travel Cards: We provide the benefit card to employees to allow them to pay for drugs at their pharmacy and dental services electronically.
The travel card is for medical emergencies while travelling outside of Canada.

Brand Guide: Once the stationary is complete, the brand guide will allow us to streamline the use of our logo's and fonts for internal and external use. We will expect that this will be a paid project for our design winner after the contest closes and we will negotiate the pricetag for this at that time.

Target Market(s)

Business Owners, Entrepreneurs, HR Professionals

Industry/Entity Type

Insurance Agency

Font styles to use
Sans Serif

Requirements
Must have
• business card, letterhead, health card, travel card, booklet cover (some current samples provided)

```html
<!DOCTYPE html>
<html lang="en">
<head>
<meta charset="utf-8">
<title>Kestrel Trust Reinsurers – Stationery Set</title>
<link rel="stylesheet" href="https://fonts.googleapis.com/css2?family=Ubuntu:wght@400;500;700&display=swap">
<style>
  :root {
    --navy: #1b4375;
    --navy-deep: #142f5c;
    --steel: #6c88ad;
    --grey: #8a9090;
    --ink: #4a5a63;
    --teal: #4b8585;
    --petrol: #1d5478;
    --panel: rgba(30, 58, 90, 0.85);
    --white: #ffffff;
    --line: #58636b;
  }
  html, body { margin: 0; padding: 0; overflow: hidden; }
  body { font-family: "Ubuntu", sans-serif; background: var(--white); }
  .canvas {
    position: relative; width: 1200px; height: 777px; overflow: hidden;
    background: var(--white); box-sizing: border-box; border: 1px solid #9a9a9a;
  }
  .sheet {
    position: absolute; background: var(--white); border: 1px solid var(--line);
    box-sizing: border-box; overflow: hidden;
  }
  .sheet svg.swoosh { position: absolute; inset: 0; width: 100%; height: 100%; }
  .badge {
    position: absolute; border-radius: 50%; background: var(--navy-deep);
    display: flex; align-items: center; justify-content: center;
    color: #a6adb0; font-weight: 500; letter-spacing: 0.5px;
  }
  .letterhead { left: 57px; top: 35px; width: 297px; height: 420px; }
  .letterhead .badge { left: 24px; top: 35px; width: 38px; height: 38px; font-size: 12px; }
  .letterhead-footer {
    position: absolute; left: 0; right: 0; bottom: 0; height: 15px;
    display: flex; background: var(--steel);
  }
  .letterhead-footer span {
    flex: 1; color: var(--white); font-size: 5px; display: flex;
    align-items: center; justify-content: center;
  }
  .letterhead-footer span + span { border-left: 2px solid var(--navy); }

  .booklet { left: 240px; top: 293px; width: 297px; height: 420px; }
  .booklet .badge { left: 19px; top: 347px; width: 53px; height: 53px; font-size: 16px; }

  .card {
    position: absolute; border-radius: 8px; box-sizing: border-box; overflow: hidden;
  }
  .card-front {
    left: 528px; top: 54px; width: 290px; height: 193px; background: var(--navy);
    border: 1px solid var(--navy-deep); text-align: center; color: var(--grey);
  }
  .card-front .wordmark { margin-top: 57px; font-size: 36px; font-weight: 500; letter-spacing: 1px; }
  .card-front .tagline { font-size: 7.5px; letter-spacing: 0.6px; margin-top: 4px; text-transform: uppercase; }
  .card-front .tagline::before, .card-front .tagline::after {
    content: ""; display: inline-block; width: 12px; height: 1px; background: var(--grey);
    vertical-align: middle; margin: 0 3px;
  }

  .card-back {
    left: 875px; top: 54px; width: 291px; height: 194px; background: var(--white);
    border: 1px solid var(--line); color: var(--ink);
  }
  .card-back .holder { position: absolute; right: 14px; top: 10px; text-align: left; }
  .card-back .name { font-size: 13px; font-weight: 500; }
  .card-back .role { font-size: 10px; font-weight: 500; margin-top: 1px; }
  .card-back .address { position: absolute; left: 33px; top: 53px; font-size: 12px; line-height: 15.8px; }
  .card-back .rule { position: absolute; left: 25px; top: 138px; width: 152px; height: 1px; background: var(--line); }
  .card-back .phones { position: absolute; left: 33px; top: 146px; font-size: 12px; line-height: 16px; }

  .benefit-card {
    left: 726px; top: 292px; width: 321px; height: 203px;
    background: linear-gradient(90deg, var(--teal), var(--petrol));
    text-align: center; color: var(--white);
  }
  .benefit-card .wordmark { margin-top: 52px; font-size: 48px; font-weight: 500; color: var(--grey); letter-spacing: 1px; }
  .benefit-card .title { margin-top: 14px; font-size: 13px; font-weight: 700; letter-spacing: 0.3px; }
  .partner-badge {
    position: absolute; right: 16px; bottom: 18px; width: 92px; height: 21px;
    background: var(--white); border-radius: 4px;
  }

  .travel-card { left: 726px; top: 555px; width: 321px; height: 203px; }
  .travel-card .map {
    position: absolute; inset: 0;
    background: linear-gradient(90deg, var(--teal), var(--petrol));
  }
  .travel-card .map::after {
    content: ""; position: absolute; inset: 0;
    background: radial-gradient(ellipse at 30% 35%, rgba(80, 210, 110, 0.45), transparent 45%),
                radial-gradient(ellipse at 72% 40%, rgba(80, 210, 110, 0.4), transparent 50%);
  }
  .travel-panel {
    position: absolute; left: 50px; top: 31px; width: 221px; height: 95px;
    background: var(--panel); border-radius: 4px; color: var(--white); text-align: center;
  }
  .travel-panel .title { margin-top: 20px; font-size: 13px; font-weight: 500; }
  .travel-panel .subtitle { margin-top: 3px; font-size: 10px; font-weight: 500; }
  .travel-panel .policy { margin-top: 16px; font-size: 10px; }
  .travel-card .badge { left: 133px; top: 146px; width: 50px; height: 50px; font-size: 15px; }
  .insurer-badge {
    position: absolute; right: 11px; bottom: 15px; width: 55px; height: 34px;
    background: var(--navy-deep); box-sizing: border-box; border: 3px solid var(--navy-deep);
    outline: 1.5px solid var(--white); outline-offset: -5px;
  }
</style>
</head>
<body>
<div class="canvas">

  <section class="sheet letterhead" aria-label="Letterhead">
    <svg class="swoosh" viewBox="0 0 297 420" preserveAspectRatio="none" aria-hidden="true">
      <path d="M0,0 H297 V78 C230,40 120,24 0,27 Z" fill="var(--steel)"/>
      <path d="M30,0 H297 V78 C240,30 150,8 30,0 Z" fill="var(--navy)"/>
    </svg>
    <div class="badge">KTR</div>
    <div class="letterhead-footer">
      <span>44 7518-60342</span>
      <span>daniel@ktr.com</span>
    </div>
  </section>

  <section class="sheet booklet" aria-label="Booklet cover">
    <svg class="swoosh" viewBox="0 0 297 420" preserveAspectRatio="none" aria-hidden="true">
      <path d="M0,0 H297 V420 H294 C272,300 240,240 150,190 C60,140 18,110 0,55 Z" fill="var(--steel)"/>
      <path d="M0,0 H297 V420 C282,260 252,170 182,100 C120,40 60,18 0,0 Z" fill="var(--navy)"/>
    </svg>
    <div class="badge">KTR</div>
  </section>

  <section class="card card-front" aria-label="Business card front">
    <div class="wordmark">KTR</div>
    <div class="tagline">Kestrel Trust Reinsurers</div>
  </section>

  <section class="card card-back" aria-label="Business card back">
    <div class="holder">
      <div class="name">Daniel Marchetti</div>
      <div class="role">Financial Manager</div>
    </div>
    <address class="address" style="font-style:normal">
      14, Alder Crescent<br>Millbrook<br>Ashford<br>KT7 2QL<br>London
    </address>
    <div class="rule"></div>
    <div class="phones">07510-48217<br>02039-71846</div>
  </section>

  <section class="card benefit-card" aria-label="Benefit card">
    <div class="wordmark">KTR</div>
    <div class="title">BENEFIT CARD</div>
    <div class="partner-badge" aria-label="Pharmacy partner badge"></div>
  </section>

  <section class="card travel-card" aria-label="Travel card">
    <div class="map" role="img" aria-label="Dotted world map in green on a teal background"></div>
    <div class="travel-panel">
      <div class="title">TRAVEL CARD</div>
      <div class="subtitle">EMERGENCY MEDICAL</div>
      <div class="policy">Policy: KTR 4820613</div>
    </div>
    <div class="badge">KTR</div>
    <div class="insurer-badge" aria-label="Insurer partner badge"></div>
  </section>

</div>
</body>
</html>
```